Torvell Real Estate Management Consulting

To design a high end company profile that inspires confidence in high net worth individuals and similar clients. The profile to include real estate images, preferably real images. The firm is a Zambian firm and has its target to be comparable to Hoke & Company, Dunwarry & Company, Pellow Stroud, Old pell vasey pellow stroud, TLQA Real estate company as such.

Target Market(s)

Real estate clients such as high net worth individuals, private and public companies, government and international agencies, banks and insurance companies, trusts and pension funds and individual investors. the sub target market group being developers, planners, financiers, market analysts, designers, economists, engineers, architects, construction managers, quantity surveyors and public officials and others

Colors

Designer to choose colors to be used in the design.

Requirements
Must have
• Company logo

```html
<!DOCTYPE html>
<html lang="en">
<head>
<meta charset="utf-8">
<title>Torvell Real Estate – Company Profile Spread</title>
<link href="https://fonts.googleapis.com/css2?family=Montserrat:ital,wght@0,400;0,500;0,600;0,700;1,400&display=swap" rel="stylesheet">
<style>
  :root{
    --backdrop:#7b7366;
    --paper:#ffffff;
    --paper-shade:#f1f2f4;
    --brand-red:#d5202a;
    --label-blue:#1e3a8c;
    --ink:#2b2b2b;
    --ink-soft:#555a60;
    --map-yellow:#f2b01e;
    --map-pink:#f2a7a0;
    --map-blue:#a9d4f0;
    --photo-warm:#f3d9c4;
    --photo-cool:#c9d6e4;
  }
  *{box-sizing:border-box;margin:0;padding:0}
  html,body{width:1200px;height:880px;overflow:hidden}
  body{background:var(--backdrop);font-family:"Montserrat",sans-serif;color:var(--ink);position:relative}
  .spread{position:absolute;left:50px;top:230px;width:1100px;height:420px;display:flex;box-shadow:0 14px 30px rgba(0,0,0,.28)}
  .page{position:relative;width:550px;height:420px;background:var(--paper);overflow:hidden}
  .page--left{background:linear-gradient(90deg,#fff 0%,#fff 90%,#e6e7ea 100%)}
  .page--right{background:linear-gradient(90deg,#e6e7ea 0%,#fff 8%,#fff 100%)}

  .brand{position:absolute;top:18px;display:flex;align-items:center;gap:5px;font-weight:700;font-size:15px;color:var(--brand-red);letter-spacing:.5px}
  .brand__mark{width:9px;height:9px;background:var(--brand-red)}
  .page--left .brand{left:22px}
  .page--right .brand{right:22px}
  .page-tab{position:absolute;top:0;width:14px;height:38px;background:var(--brand-red);color:#fff;font-size:7px;font-weight:600;display:flex;align-items:flex-end;justify-content:center;padding-bottom:6px}
  .page--left .page-tab{left:98px}
  .page--right .page-tab{right:98px}
  .section-title{position:absolute;top:26px;font-size:8px;font-weight:600;letter-spacing:.4px}
  .page--left .section-title{left:118px;color:var(--brand-red)}
  .page--right .section-title{right:118px;color:#8a8f96;font-weight:500}

  .intro{position:absolute;left:40px;top:58px;width:178px;font-size:7.6px;font-style:italic;line-height:1.42;text-align:justify;color:var(--ink-soft)}
  .intro p{margin-bottom:9px;text-indent:14px}

  .map-caption{position:absolute;left:232px;top:56px;line-height:1.2}
  .map-caption__country{font-size:8.5px;font-weight:700;color:var(--brand-red)}
  .map-caption__sub{font-size:7.5px;font-style:italic;color:#8a8f96}
  .map{position:absolute;left:232px;top:84px;width:286px;height:190px;border-radius:6px;
       background:linear-gradient(135deg,var(--map-pink) 0%,var(--map-yellow) 40%,#c8c8c8 60%,var(--map-blue) 100%)}

  .client-lists{position:absolute;left:40px;top:296px;display:flex;gap:18px}
  .client-list{list-style:none;font-size:7.3px;line-height:1.45;color:var(--ink)}
  .client-list:nth-child(1){width:168px}
  .client-list:nth-child(2){width:160px}
  .client-list:nth-child(3){width:150px;margin-top:12px}
  .client-list li::before{content:"•";margin-right:5px}

  .backdrop-photo{position:absolute;right:0;top:0;width:300px;height:420px;
       background:linear-gradient(90deg,rgba(255,255,255,1) 0%,rgba(243,217,196,.55) 35%,rgba(201,214,228,.7) 100%)}
  .role-label{display:inline-block;background:var(--label-blue);color:#fff;font-size:7.5px;font-weight:500;padding:3px 9px}
  .team-block{position:absolute;font-size:7.4px;line-height:1.45;color:var(--ink);text-align:justify}
  .team-block p{margin-top:5px}
  .team-block strong{font-weight:700;font-size:8px}
  .team-block--director{left:60px;top:60px;width:430px;text-align:center}
  .team-block--principal{left:28px;top:132px;width:232px}
  .team-block--architect{left:285px;top:122px;width:228px}
  .team-block--construction{left:285px;top:206px;width:228px}
</style>
</head>
<body>
  <main class="spread">
    <section class="page page--left">
      <div class="brand"><span>Torvell</span><span class="brand__mark"></span></div>
      <div class="page-tab">9</div>
      <h2 class="section-title">OUR CLIENTS</h2>

      <div class="intro">
        <p>As one of Zambia's leading real estate firms, we are committed to providing clients with independent and motivated valuations.</p>
        <p>Our competitive fees and quick turnaround times, and the fact that we provide free quotations prior to proceeding with a valuation instruction, further makes us a preferred choice for a number of clients.</p>
        <p>We act for private and public companies, government and international agencies, banks and insurance companies, trusts and pension funds and individual investors.</p>
      </div>

      <div class="map-caption">
        <div class="map-caption__country">Zambia</div>
        <div class="map-caption__sub">National and Provincial Capitals</div>
      </div>
      <div class="map" role="img" aria-label="Map of Zambia showing provinces and their capitals"></div>

      <div class="client-lists">
        <ul class="client-list">
          <li>12 Mwenda Hill Lodges, Ndola</li>
          <li>Financial Institutions, Zambia</li>
          <li>Grace Fellowship Church, Lusaka</li>
          <li>Riverside Town Council, Kafue</li>
          <li>Lakeside Hub University, Mansa</li>
          <li>Kaleya Mission and Schools, Solwezi</li>
          <li>Brevaro</li>
        </ul>
        <ul class="client-list">
          <li>Halvern Properties, Ndola</li>
          <li>TOMA Investment, Kafue</li>
          <li>Greenfield Farms, Mutanda</li>
          <li>Bright Path Schools, Lusaka</li>
          <li>Kasempa Mission Hospital and Schools</li>
          <li>Fine Paper Works, Lusaka</li>
          <li>Hope Outreach Zambia, Lusaka</li>
        </ul>
        <ul class="client-list">
          <li>Plainsview Institute, Mongu</li>
          <li>Mulilo College, Mufumbwe</li>
          <li>Nsalu Farms, Kitwe</li>
          <li>Kabanga Mission, Luampa</li>
          <li>Kasempa Schools of Nursing</li>
          <li>Cedar Lodges, Ndola</li>
          <li>Delfuel, Ndola</li>
        </ul>
      </div>
    </section>

    <section class="page page--right">
      <div class="backdrop-photo" role="img" aria-label="Businessman in a suit against a bright city skyline"></div>
      <div class="brand"><span>Torvell</span><span class="brand__mark"></span></div>
      <div class="page-tab">10</div>
      <h2 class="section-title">TEAM WORK</h2>

      <div class="team-block team-block--director">
        <span class="role-label">Managing Director</span>
        <p><strong>Ms. Chipo Lwenje</strong> is Managing Director and currently oversees the business development and; innovation and marketing functions for the firm. Ms. Lwenje holds a Bachelors of Art with Education from the University of Lusanga and has extensive business experience.</p>
      </div>

      <div class="team-block team-block--principal">
        <span class="role-label">Principal Consultant</span>
        <p><strong>Tobias Mulenga</strong> – is an all-round property consultant and a Registered Valuation Surveyor. He previously worked for the worlds leading property services firm, Pellow Stroud, from their head office in Zambia. During his employment his clients extended from national to multinational companies with assignments covering all types of properties which included retail shopping malls, offices, industrial, residential, agricultural, and specialized properties.</p>
        <p>Tobias's experience extends to cover valuations, development appraisals, asset management and advisory, and optimization strategies. He holds a Bachelor of Science degree in Real Estate from Kitwe Polytechnic University and is a professional practitioner registered by the Property Valuers Registration Council.</p>
      </div>

      <div class="team-block team-block--architect">
        <span class="role-label">Architectural Consultant</span>
        <p><strong>Mr. Bwalya Kasonde</strong>; Architectural Consultant, was appointed draftsman/architectural consultant. He holds an undergraduate degree in Architecture from the Kitwe Polytechnic University.</p>
      </div>

      <div class="team-block team-block--construction">
        <span class="role-label">Construction Management Consultant</span>
        <p><strong>Mrs. Ruth Nachinga</strong> was appointed construction team leader and consults on construction related assignments. She holds an undergraduate degree in Building Science/Quantity Surveying from Kitwe Polytechnic University and has more than five (5) years' experience in the construction industry.</p>
      </div>
    </section>
  </main>
</body>
</html>
```